Career Ad - Graphic Image to Attract New Team Members to our Company

We would like a career ad to be used for recruiting staff. This ad will be posted through our social media sites and may also be printed on post cards. Concept we like so far (however we are open to other creative ideas) is a photo in the background with printing on top. The color would be our brand color : blue. As for content, words like "We're Hiring" or "Come join our team" we'd also like to have reference to our website https://lindenvale.ca/about/careers and our email careers@lindenvale.ca Of course, our logo and company name, which is attached in the files
Target Market(s)
Professional
Requirements
Must have
- company logo
Nice to have
- visually apealling

```html
<!DOCTYPE html>
<html lang="en">
<head>
<meta charset="utf-8">
<title>Come Join Our Team – Lindenvale Brokers</title>
<link rel="stylesheet" href="https://fonts.googleapis.com/css2?family=Open+Sans:wght@400;600;700&display=swap">
<style>
  :root {
    --paper: #f3f3f3;
    --navy: #1f2660;
    --royal: #2a4fae;
    --lavender: #cbcde6;
  }
  html, body {
    margin: 0;
    padding: 0;
    overflow: hidden;
    background: var(--paper);
  }
  .career-ad {
    position: relative;
    width: 1200px;
    height: 960px;
    background: var(--paper);
    overflow: hidden;
    font-family: "Open Sans", "Segoe UI", sans-serif;
  }
  .career-ad__artwork {
    position: absolute;
    left: 216px;
    top: 88px;
    width: 768px;
    height: 484px;
  }
  .career-ad__headline {
    position: absolute;
    left: 0;
    right: 0;
    top: 206px;
    margin: 0;
    text-align: center;
    color: var(--navy);
    font-weight: 600;
    font-size: 146px;
    line-height: 146px;
    letter-spacing: -1px;
    text-transform: uppercase;
  }
  .career-ad__contact {
    position: absolute;
    left: 0;
    right: 0;
    top: 604px;
    margin: 0;
    text-align: center;
    color: var(--royal);
    font-weight: 400;
    font-size: 36px;
    line-height: 51px;
    font-style: normal;
  }
  .career-ad__contact span { display: block; }
  .brand-footer__rule {
    position: absolute;
    top: 883px;
    height: 4px;
    width: 328px;
    background: var(--navy);
  }
  .brand-footer__rule--left { left: 80px; }
  .brand-footer__rule--right { left: 791px; }
  .brand-footer__dot {
    position: absolute;
    left: 574px;
    top: 790px;
    width: 52px;
    height: 52px;
    border-radius: 50%;
    background: var(--navy);
  }
  .brand-footer__name {
    position: absolute;
    left: 0;
    right: 0;
    top: 866px;
    margin: 0;
    text-align: center;
    color: var(--navy);
    font-weight: 700;
    font-size: 28px;
    line-height: 38px;
    letter-spacing: 1px;
  }
</style>
</head>
<body>
  <main class="career-ad">
    <svg class="career-ad__artwork" role="img" aria-label="Faint lavender illustration of two hands meeting in a handshake" viewBox="0 0 768 484">
      <defs>
        <radialGradient id="artwork-tone" cx="50%" cy="48%" r="60%">
          <stop offset="0%" stop-color="#cbcde6"/>
          <stop offset="75%" stop-color="#cbcde6" stop-opacity="0.85"/>
          <stop offset="100%" stop-color="#cbcde6" stop-opacity="0"/>
        </radialGradient>
      </defs>
      <rect x="0" y="0" width="768" height="484" rx="120" fill="url(#artwork-tone)"/>
    </svg>

    <h1 class="career-ad__headline">Come Join<br>Our Team!</h1>

    <address class="career-ad__contact">
      <span>Visit us at:</span>
      <span>https://lindenvale.ca/about/careers</span>
      <span>careers@lindenvale.ca</span>
    </address>

    <footer class="brand-footer">
      <div class="brand-footer__rule brand-footer__rule--left"></div>
      <div class="brand-footer__dot"></div>
      <p class="brand-footer__name">LINDENVALE BROKERS</p>
      <div class="brand-footer__rule brand-footer__rule--right"></div>
    </footer>
  </main>
</body>
</html>
```